Luxury 8’x4’ Acreage FOR SALE sign

I need (in 3 days) an outstanding Luxury - looking For Sale sign with my logo prominent & my brokerage logo to make up 9% of the total design space. It also needs to have “space” around it to breathe (as per brokerage qualification boundaries) It needs to be unique , have my phone number , my logo (with or without Real Estate cropped out) , brokerage logo & “for sale” or “available” or some type of wording that projects it’s a sign listing an acreage. My main focus is branding - MY logo & brand being recognized. I am unsure about including a photo of myself or not as I need this to look sleek & not busy! I have included a photo of the sign I designed & it’s just not doing it for me … I DO NOT want it to look like a business card. I’m finding it hard to make it look intentional with the DVK logo needed. It can be either logo - the box logo or the horizontal DVK logo but MUST make up 9%.
Updates

No photo of me please ! Decision made!

Target Market(s)

Luxury

Industry/Entity Type

Real Estate

Requirements
Must have
• Phone number, My logo, My Brokerage logo
Nice to have
• Needs to stand out “for sale” or “available” or

```html
<!DOCTYPE html>
<html lang="en">
<head>
<meta charset="UTF-8">
<title>Reid Kestow Real Estate – For Sale Sign</title>
<link rel="stylesheet" href="https://fonts.googleapis.com/css2?family=Cinzel:wght@400;600;700&display=swap">
<style>
  :root {
    --backdrop: #dcdcdc;
    --sign-black: #050608;
    --text-white: #ffffff;
    --brokerage-grey: #6a6c70;
    --gold-light: #f2e27c;
    --gold-deep: #c99a2e;
  }
  html, body {
    margin: 0;
    padding: 0;
    width: 1200px;
    height: 1200px;
    overflow: hidden;
    background: var(--backdrop);
  }
  .sign {
    position: absolute;
    left: 0;
    top: 299px;
    width: 1200px;
    height: 602px;
    background: var(--sign-black);
    font-family: "Cinzel", "Times New Roman", serif;
    color: var(--text-white);
  }
  .listing-status {
    position: absolute;
    left: 50px;
    top: 190px;
    margin: 0;
    font-size: 54px;
    font-weight: 400;
    letter-spacing: 0.2em;
    line-height: 1;
  }
  .agent-phone {
    position: absolute;
    left: 48px;
    top: 274px;
    margin: 0;
    font-size: 70px;
    font-weight: 400;
    line-height: 1;
    letter-spacing: -0.01em;
  }
  .brokerage {
    position: absolute;
    left: 50px;
    top: 390px;
    display: flex;
    align-items: center;
    gap: 16px;
  }
  .brokerage-dot {
    width: 22px;
    height: 22px;
    border-radius: 50%;
    background: var(--gold-deep);
  }
  .brokerage-name {
    font-size: 34px;
    font-weight: 400;
    color: var(--brokerage-grey);
    letter-spacing: 0.08em;
    line-height: 1;
  }
  .divider {
    position: absolute;
    left: 582px;
    top: 113px;
    width: 2px;
    height: 375px;
    background: linear-gradient(to bottom, transparent, var(--gold-deep) 35%, var(--gold-light) 50%, var(--gold-deep) 65%, transparent);
  }
  .agent-brand {
    position: absolute;
    left: 640px;
    top: 180px;
    width: 515px;
    font-weight: 700;
    color: var(--text-white);
    line-height: 1;
  }
  .agent-first {
    display: block;
    text-align: right;
    font-size: 94px;
  }
  .agent-last {
    display: block;
    text-align: right;
    font-size: 108px;
    margin-top: 2px;
  }
  .agent-tagline {
    display: block;
    text-align: right;
    font-size: 44px;
    letter-spacing: 0.42em;
    margin-right: -0.42em;
    margin-top: 10px;
  }
</style>
</head>
<body>
  <main class="sign">
    <h1 class="listing-status">FOR SALE</h1>
    <p class="agent-phone">403-555-0142</p>
    <div class="brokerage">
      <span class="brokerage-dot"></span>
      <span class="brokerage-name">DVK REALTY</span>
    </div>
    <div class="divider"></div>
    <div class="agent-brand">
      <span class="agent-first">REID</span>
      <span class="agent-last">KESTOW</span>
      <span class="agent-tagline">REAL ESTATE</span>
    </div>
  </main>
</body>
</html>
```